Quiet Lanterns: Reflections on Tide Charts and Orchard Rituals Among Coastal Villages.

Book cover, spine, and back cover. This is written by Dr. T. HALVERSEN, and will be an educational book for academics, government officials, and the general population.
I'm imagining the outline of a person with am active mind in the middle. It would be overlayed on top of a circular galaxy on the background. On either side, smaller, perhaps in the background would be a cross on one side and a few uaps (ufo) of different shapes on the other (orb, saucer, triangle. ) beneath allnof this would be something symbolizing society - either the earth itself or the skyline of a large city.
By Dr. T. HALVERSEN along the bottom, i presume. (Ai cannot make this, but I've included a few examples nonetheless. )
I assume I will be given the opportunity to write a synopsis on the back cover. I will be self publishing and selling from my website.
Target Market(s)
Academics, professionals, church leaders, government officials, and the general public.
Industry/Entity Type
Professional and community education
Requirements
Must have
- It should look like a ph.d level book. Eye catching but not overly fantastical. (Its an educational book not a comic book)
Should not have
- Not hollywood or fantasy book looking. It should look a graduate school book. The tone is quite serious.

```html
<!DOCTYPE html>
<html lang="en">
<head>
<meta charset="utf-8">
<title>Quiet Lanterns – Cover Layout</title>
<link href="https://fonts.googleapis.com/css2?family=Libre+Baskerville&family=Playfair+Display:wght@400;700&family=Open+Sans:wght@400;700&display=swap" rel="stylesheet">
<style>
  :root {
    --page: #ffffff;
    --bleed: #f2a98f;
    --trim-line: #8a5a50;
    --night: #060b1f;
    --deep-blue: #0d2450;
    --ring-blue: #4fb6f0;
    --ember: #f07a24;
    --glow: #ffd76a;
    --band: rgba(30, 30, 45, 0.55);
    --type-light: #ffffff;
    --note-ink: #1c1c1c;
    --note-grey: #8c8c8c;
    --barcode-yellow: #f7ea00;
  }
  * { box-sizing: border-box; margin: 0; padding: 0; }
  html, body {
    width: 745px; height: 1200px; overflow: hidden;
    background: var(--page);
  }
  .canvas { position: relative; width: 745px; height: 1200px; }

  /* ---------- front cover ---------- */
  .cover {
    position: absolute;
    width: 392px; height: 594px;
    overflow: hidden;
    color: var(--type-light);
  }
  .cover--hero { left: 177px; top: 63px; }
  .cover--mini { left: 391px; top: 724px; transform: scale(0.643); transform-origin: 0 0; }

  .cover__art {
    position: absolute; inset: 0;
    background:
      radial-gradient(circle at 50% 30%, var(--glow) 0 4%, var(--ember) 14%, rgba(240,122,36,0) 30%),
      radial-gradient(circle at 50% 36%, rgba(0,0,0,0) 38%, rgba(79,182,240,0.9) 39.5%, rgba(200,150,190,0.55) 44%, rgba(79,182,240,0.35) 50%, rgba(13,36,80,0) 56%),
      radial-gradient(ellipse at 50% 95%, #05070f 0 30%, rgba(5,7,15,0) 60%),
      radial-gradient(circle at 50% 40%, var(--deep-blue) 0%, var(--night) 75%);
  }
  .cover__band {
    position: absolute; left: 0; right: 0; top: 46px; height: 41px;
    background: var(--band);
  }
  .cover__subtitle {
    position: absolute; left: 0; right: 0; top: 52px;
    font-family: "Libre Baskerville", serif;
    font-size: 12.4px; line-height: 17px;
    text-align: center; letter-spacing: 0.4px;
  }
  .cover__title {
    position: absolute; left: 0; right: 0; top: 430px;
    font-family: "Playfair Display", serif;
    text-align: center; line-height: 1;
  }
  .cover__title-top { display: block; font-size: 35px; font-weight: 400; letter-spacing: 0.5px; }
  .cover__title-main { display: block; font-size: 45px; font-weight: 700; letter-spacing: 4px; margin-top: 2px; }
  .cover__author {
    position: absolute; left: 0; right: 0; top: 544px;
    font-family: "Playfair Display", serif;
    font-size: 14px; text-align: center;
  }
  .cover__author b { font-weight: 700; }

  /* ---------- print template ---------- */
  .template {
    position: absolute; left: 92px; top: 714px;
    width: 561px; height: 402px;
    background: var(--bleed);
  }
  .trim-line {
    position: absolute; left: 5px; top: 5px; right: 5px; bottom: 5px;
    border: 1px dashed var(--trim-line);
  }
  .fold-line {
    position: absolute; top: 0; bottom: 0; width: 0;
    border-left: 1px dashed var(--trim-line);
  }
  .fold-line--left { left: 266px; }
  .fold-line--right { left: 294px; }

  .back-panel {
    position: absolute; left: 10px; top: 10px; width: 251px; height: 382px;
    background: var(--page);
    font-family: "Open Sans", sans-serif; color: var(--note-ink);
  }
  .spec-list { position: absolute; left: 17px; top: 40px; width: 225px; }
  .spec { margin-bottom: 7px; font-size: 4.3px; line-height: 5.6px; }
  .spec__head { font-size: 5.6px; font-weight: 700; line-height: 7px; }
  .spec__metric { color: var(--note-grey); }
  .back-size {
    position: absolute; left: 6px; bottom: 6px;
    font-size: 4.3px; line-height: 5.4px; color: var(--note-grey);
  }
  .barcode-zone {
    position: absolute; left: 158px; top: 334px; width: 88px; height: 52px;
    background: var(--barcode-yellow);
    display: flex; align-items: center; justify-content: center; text-align: center;
    font-size: 7px; font-weight: 700; line-height: 10.5px; color: #3a3a3a;
  }

  .spine-panel {
    position: absolute; left: 269px; top: 10px; width: 22px; height: 382px;
    background: var(--page);
  }
  .spine-note {
    position: absolute; left: 8px; bottom: 4px;
    writing-mode: vertical-rl;
    font-family: "Open Sans", sans-serif; font-size: 4.3px; color: var(--note-grey);
    white-space: nowrap;
  }
</style>
</head>
<body>
<main class="canvas">

  <section class="cover cover--hero">
    <div class="cover__art" role="img" aria-label="Illustration of a luminous human head outline with a glowing mind, set before a circular galaxy ring and distant craft in a starry sky"></div>
    <div class="cover__band"></div>
    <p class="cover__subtitle">REFLECTIONS ON TIDE CHARTS AND ORCHARD<br>RITUALS AMONG COASTAL VILLAGES.</p>
    <h1 class="cover__title"><span class="cover__title-top">QUIET</span><span class="cover__title-main">LANTERNS</span></h1>
    <p class="cover__author">Dr. <b>T. HALVERSEN</b></p>
  </section>

  <section class="template">
    <div class="back-panel">
      <div class="spec-list">
        <div class="spec"><div class="spec__head">Page Layout Size = Print Sheet Size</div>&nbsp;&nbsp;&nbsp;19"(w) X 13"(h) <span class="spec__metric">(482.6mm x 330.2mm)</span></div>
        <div class="spec"><div class="spec__head">Black Dotted Line = Trim Edge</div>The trim size of this book including spine -<br>&nbsp;&nbsp;&nbsp;<b>12.64" x 9.0"</b> <span class="spec__metric">(321.06mm x 228.6mm)</span></div>
        <div class="spec"><div class="spec__head">Blue Dotted Line = Spine Fold</div>Fold placement may vary slightly.</div>
        <div class="spec"><div class="spec__head">White Area = Live Area</div>Position logos, text, and essential images in this area.</div>
        <div class="spec"><div class="spec__head">Red Area = Out of Live/Bleed</div>Your background artwork must fill the red area. Do not place logos, text, or essential images in the red area. If your artwork does not meet these requirements, it may be rejected.</div>
      </div>
      <div class="barcode-zone">Barcode<br>Location &amp; Size<br>2" X 1.2"</div>
      <div class="back-size">Back<br>6.0" x 9.0"<br>(152.4mm x 228.6mm)</div>
    </div>
    <div class="spine-panel"><span class="spine-note">Spine Width: 0.64" (16.26mm)</span></div>
    <div class="trim-line"></div>
    <div class="fold-line fold-line--left"></div>
    <div class="fold-line fold-line--right"></div>
  </section>

  <section class="cover cover--mini">
    <div class="cover__art" role="img" aria-label="Front cover illustration: luminous human head outline with a glowing mind before a circular galaxy ring"></div>
    <div class="cover__band"></div>
    <p class="cover__subtitle">REFLECTIONS ON TIDE CHARTS AND ORCHARD<br>RITUALS AMONG COASTAL VILLAGES.</p>
    <h2 class="cover__title"><span class="cover__title-top">QUIET</span><span class="cover__title-main">LANTERNS</span></h2>
    <p class="cover__author">Dr. <b>T. HALVERSEN</b></p>
  </section>

</main>
</body>
</html>
```